Business Card Design Project

Name Martin Hollowell
Company Pinebrook Hazard Recovery Crew
address 27/3 Korvenado street
Acacia Ridge
Brisbane Queensland
Australia 4110,
0487352916

Things that we do Mould inspection and Remediation,
Crime and Trauma Scene Cleanup and Decontamination
Drug lab Decontamination and needle cleanups.
Odor control
Air quality Testing and swabs,
latest equipment
Hydroxyl machines, ozone machines ,Sterilising lights ,Comercial Steam machines ,
Thermal imaging, Bacteria testing equipment
Fully trained personel

Reason: One day is not enough time to get designs i dont why the Current deadline is only one day

I do not need vanta wipe in the cards, that was only a sample, The Business name isĀ 

Pinebrook Hazard Recovery Crew.

Target Market(s)

Government agencies ,Police and real-estates, housing companies, Coroners

Industry/Entity Type

Business

Requirements
Must have
• Must tell what we are about
Nice to have
• raised letters or good background

```html
<!DOCTYPE html>
<html lang="en">
<head>
<meta charset="utf-8">
<title>Pinebrook Hazard Recovery Crew – Business Card</title>
<link rel="stylesheet" href="https://fonts.googleapis.com/css2?family=Arimo:wght@700&family=Cinzel:wght@400;600&family=Josefin+Sans:wght@400&display=swap">
<style>
  :root {
    --page-bg: #e9e6e0;
    --card-white: #ffffff;
    --ochre-dark: #8a6d22;
    --ochre-mid: #b28f34;
    --ochre-light: #cfae52;
    --name-yellow: #c4be1c;
    --ink: #1e1e1e;
    --smoke-yellow: #d9d23a;
    --smoke-pale: #f4f1b8;
    --back-text: #ffffff;
  }
  * { margin: 0; padding: 0; box-sizing: border-box; }
  html, body {
    width: 1200px;
    height: 785px;
    overflow: hidden;
    background: var(--page-bg);
  }
  .canvas {
    position: relative;
    width: 1200px;
    height: 785px;
  }
  .card {
    position: absolute;
    left: 300px;
    width: 600px;
    height: 343px;
    overflow: hidden;
    box-shadow: 0 6px 18px rgba(0, 0, 0, 0.18);
  }

  /* Back side: services list */
  .card-back {
    top: 30px;
  }
  .back-texture {
    position: absolute;
    inset: 0;
    background: linear-gradient(135deg, var(--ochre-light) 0%, var(--ochre-mid) 50%, var(--ochre-dark) 100%);
  }
  .services {
    position: absolute;
    inset: 0;
    display: flex;
    flex-direction: column;
    justify-content: center;
    align-items: center;
    list-style: none;
    font-family: "Arimo", sans-serif;
    font-weight: 700;
    font-size: 15px;
    line-height: 1.45;
    color: var(--back-text);
    text-align: center;
    text-shadow: 0 1px 2px rgba(0, 0, 0, 0.35);
  }

  /* Front side: name, company, address */
  .card-front {
    top: 412px;
    background: var(--card-white);
  }
  .smoke {
    position: absolute;
    top: 0;
    right: 0;
    width: 150px;
    height: 100%;
    background: linear-gradient(160deg, var(--smoke-pale) 0%, var(--smoke-yellow) 45%, #8f8a1a 70%, var(--smoke-pale) 100%);
  }
  .holder-name {
    position: absolute;
    left: 40px;
    top: 70px;
    font-family: "Cinzel", serif;
    font-weight: 600;
    font-size: 24px;
    color: var(--name-yellow);
    letter-spacing: 0.5px;
  }
  .company {
    position: absolute;
    left: 220px;
    top: 80px;
    width: 230px;
    display: flex;
    flex-direction: column;
    align-items: center;
    gap: 14px;
  }
  .company-mark {
    width: 42px;
    height: 42px;
    background: var(--name-yellow);
  }
  .company-name {
    font-family: "Cinzel", serif;
    font-weight: 400;
    font-size: 14px;
    color: var(--ink);
    text-align: center;
    letter-spacing: 0.5px;
  }
  .address {
    position: absolute;
    left: 40px;
    top: 180px;
    font-family: "Josefin Sans", sans-serif;
    font-style: normal;
    font-size: 19px;
    line-height: 1.35;
    color: var(--ink);
  }
</style>
</head>
<body>
<main class="canvas">

  <section class="card card-back" aria-label="Card back: services">
    <div class="back-texture" role="img" aria-label="Ochre background with faint handwritten notes texture"></div>
    <ul class="services">
      <li>Mould inspection and Remediation,</li>
      <li>Crime and Trauma Scene Cleanup and Decontamination</li>
      <li>Drug lab Decontamination and needle cleanups.</li>
      <li>Odor control</li>
      <li>Air quality Testing and swabs,</li>
      <li>latest equipment</li>
      <li>Hydroxyl machines, ozone machines ,Sterilising lights</li>
      <li>,Comecial Steam machines ,</li>
      <li>Thermal imaging, Bacteria testing equipment</li>
      <li>Fully trained personel</li>
    </ul>
  </section>

  <section class="card card-front" aria-label="Card front: contact details">
    <div class="smoke" role="img" aria-label="Swirling yellow and black smoke illustration"></div>
    <h1 class="holder-name">Martin Hollowell</h1>
    <div class="company">
      <span class="company-mark"></span>
      <p class="company-name">Pinebrook Hazard Recovery Crew</p>
    </div>
    <address class="address">
      27/3 Korvenado street<br>
      Acacia Ridge<br>
      Brisbane Queensland<br>
      Australia 4110,<br>
      0487352916
    </address>
  </section>

</main>
</body>
</html>
```